Flyer Design

brisk-wave "logo to be bold but in small case letters"
Would like background to be metallic foil and logo and writing to be bright orange
independent pressure cleaning company
Cleaning and refurbishment of paving and patios and decking
Please phone our freephone number for a free estimate
I would like to use first image 2nd and 3rd if possible
Would like image to be bright sharp and bold.

Target Market(s)

home owners, driveways, patio cleaning, decking cleaning

Industry/Entity Type

Pressure Cleaning

Requirements
Must have
• freephone number 08084729316
email address : briskwaver@mailnest.example
Should not have
• Not too cramped

```html
<!DOCTYPE html>
<html lang="en">
<head>
<meta charset="utf-8">
<title>brisk-wave – Pressure Washing Flyer</title>
<link href="https://fonts.googleapis.com/css2?family=Oswald:wght@600;700&family=Arimo:ital,wght@0,400;0,700;1,400&display=swap" rel="stylesheet">
<style>
  :root {
    --brown: #3b2419;
    --orange: #ef8a1e;
    --orange-light: #f7b347;
    --yellow: #f6e80a;
    --white: #ffffff;
  }
  html, body {
    margin: 0;
    padding: 0;
    overflow: hidden;
    background: var(--brown);
  }
  .flyer {
    position: relative;
    width: 844px;
    height: 1200px;
    overflow: hidden;
    background: var(--brown);
    font-family: "Arimo", Arial, sans-serif;
    color: var(--white);
  }
  .backdrop {
    position: absolute;
    inset: 0;
  }
  .brand {
    position: absolute;
    top: 52px;
    left: 0;
    width: 100%;
    display: flex;
    justify-content: center;
    align-items: center;
    gap: 14px;
  }
  .brand-dot {
    width: 22px;
    height: 22px;
    border-radius: 50%;
    background: var(--orange);
  }
  .brand-name {
    font-weight: 700;
    font-size: 64px;
    line-height: 72px;
    color: var(--orange);
    text-transform: lowercase;
  }
  .tagline {
    position: absolute;
    top: 158px;
    width: 100%;
    margin: 0;
    text-align: center;
    font-style: italic;
    font-size: 18px;
  }
  .headline {
    position: absolute;
    top: 198px;
    width: 100%;
    margin: 0;
    text-align: center;
    font-family: "Oswald", Impact, sans-serif;
    font-weight: 700;
    font-size: 39px;
    line-height: 50px;
    color: var(--yellow);
  }
  .services-title {
    position: absolute;
    top: 764px;
    left: 42px;
    width: 180px;
    margin: 0;
    text-align: center;
    font-family: "Oswald", Impact, sans-serif;
    font-weight: 600;
    font-size: 30px;
    line-height: 41px;
    color: var(--orange);
  }
  .services-list {
    position: absolute;
    top: 896px;
    left: 10px;
    width: 250px;
    margin: 0;
    padding: 0;
    list-style: none;
    text-align: center;
    font-weight: 700;
    font-size: 23px;
    line-height: 35.5px;
  }
  .work-photo {
    position: absolute;
    top: 904px;
    height: 128px;
  }
  .work-photo--paving { left: 266px; width: 172px; background: linear-gradient(160deg, #5b4a44, #2f2a2a 60%, #8a5a48); }
  .work-photo--washing { left: 447px; width: 128px; background: linear-gradient(180deg, #4e6b3a, #7d7d76 55%, #a9a49a); }
  .work-photo--patio { left: 584px; width: 260px; background: linear-gradient(170deg, #566b3c, #b9a98c 45%, #d1c2a6); }
  .promise {
    position: absolute;
    top: 1055px;
    width: 100%;
    margin: 0;
    text-align: center;
    font-size: 17px;
    line-height: 23.5px;
  }
  .promise-call {
    display: block;
    font-weight: 700;
    color: var(--orange);
  }
  .contact-bar {
    position: absolute;
    left: 40px;
    top: 1135px;
    width: 772px;
    height: 65px;
    box-sizing: border-box;
    padding: 0 24px;
    border-radius: 30px 30px 0 0;
    background: var(--orange);
    display: flex;
    align-items: center;
    justify-content: center;
    font-size: 32px;
    white-space: nowrap;
  }
</style>
</head>
<body>
<div class="flyer">
  <svg class="backdrop" width="844" height="1200" viewBox="0 0 844 1200" aria-hidden="true">
    <defs>
      <linearGradient id="patio-tone" x1="0" y1="0" x2="0" y2="1">
        <stop offset="0" stop-color="#4f7a3a"/>
        <stop offset="0.5" stop-color="#6f8f4b"/>
        <stop offset="0.75" stop-color="#d98a4e"/>
        <stop offset="1" stop-color="#e0925a"/>
      </linearGradient>
    </defs>
    <path class="swoosh-light" d="M0,150 C150,250 280,340 480,346 C640,350 760,316 844,296 L844,700 L0,700 Z" fill="var(--orange-light)"/>
    <path class="swoosh-main" d="M0,166 C150,266 280,356 480,362 C640,366 760,332 844,312 L844,700 L0,700 Z" fill="var(--orange)"/>
    <path class="swoosh-rim" d="M0,192 C150,292 280,382 480,388 C640,392 760,358 844,338 L844,700 L0,700 Z" fill="var(--white)"/>
    <path class="hero-photo" role="img" aria-label="Photo of a clean terracotta-tiled patio with white wicker chairs and a glass table, surrounded by green hedges and palm fronds" d="M0,200 C150,300 280,390 480,396 C640,400 760,366 844,346 L844,770 C650,735 380,700 0,735 Z" fill="url(#patio-tone)"/>
    <path class="swoosh-rim" d="M0,728 C380,692 650,728 844,762 L844,772 C650,740 380,706 0,740 Z" fill="var(--white)"/>
    <path class="swoosh-light" d="M0,738 C380,704 650,738 844,770 L844,800 C650,770 380,730 0,752 Z" fill="var(--orange-light)"/>
    <path class="swoosh-main" d="M0,748 C380,718 650,760 844,792 L844,856 C660,840 380,760 0,760 Z" fill="var(--orange)"/>
  </svg>

  <header class="brand">
    <span class="brand-dot"></span>
    <span class="brand-name">brisk-wave</span>
  </header>
  <p class="tagline">The Pressure washing company</p>

  <h1 class="headline">Providing you with a Healthy &amp;<br>clean environment.</h1>

  <h2 class="services-title">Affordable Cleaning Services</h2>
  <ul class="services-list">
    <li>• Driveway • Patio</li>
    <li>• Decking cleaning</li>
    <li>&amp; Refurbishment</li>
    <li>• Sealing</li>
  </ul>

  <div class="work-photo work-photo--paving" role="img" aria-label="Photo of a rotary surface cleaner on block paving, showing a cleaned strip"></div>
  <div class="work-photo work-photo--washing" role="img" aria-label="Photo of a worker pressure washing a driveway"></div>
  <div class="work-photo work-photo--patio" role="img" aria-label="Photo of a freshly cleaned sandstone garden patio"></div>

  <p class="promise">We Provide a High Quality cleaning service<br>at competitive price throughout " your" Area!<span class="promise-call">Call Now for a free Estimate</span></p>

  <footer class="contact-bar">08084729316 | briskwaver@mailnest.example</footer>
</div>
</body>
</html>
```